We’re a real estate firm that has landed a big builder in a neighboring state. Our branding needs...

We are a real estate firm who represents various builders along with doing resale here in Oregon. Our firm is growing to represent a big builder in Washington State and we’ll have another 40 brokers on our team. We need rebranding. As in, a new logo ( the house logo we have now looks cartoonish, hate it). We need new cards, something to really stand out. I’ve been thinking of using those NFC cards from ZIB or the ones with the seam color. I likely want two or three designs, a darker (as in a background color of black or grey) , a light one ( again I mean background color) and a credit card style (either plastic w an embossed name/number on front, or metal ). I’m thinking dark background for cc, or silver if it’s metal. That’s my thoughts, but you are the artists, so maybe you have an idea I haven’t considered. Our colors were black and red, but we don’t have to stick to that. Just nothing too busy. Oh, and we are typically representing the local, higher quality builders in our area (just below custom), but not national. Subdivisions are near the Kel Varsby, Tobrin, and Ashfield Coastal sites. We are super excited, but without a lot of time to change the “look” of our brokerage. So I’ll be deciding and moving forward within 24 hours tops. Our name is Real Estate Summitline Partners ( we cant change the name because of timeline and business license) Thank you!

Industry/Entity Type

Real Estate

Contact Information for Business Card

The usual. Name of firm. Name of cardholder. Contact info.

Font styles to use
Serif
Sans Serif

Colors

Designer to choose colors to be used in the design.

Requirements
Must have
• A sleek or simple look. I included photos of cards with stylistic attributes we like. Thank you
Nice to have
• We really like the black backgrounds. With foil or embossed detail. We also like the black on black. Matte black card with raised shiny black detail. But still eye catching.
Should not have
• No ornate or busy looking style. We don’t want anything cluttered.

```html
<!DOCTYPE html>
<html lang="en">
<head>
<meta charset="utf-8">
<title>Real Estate Summitline Partners – Business Card</title>
<link rel="stylesheet" href="https://fonts.googleapis.com/css2?family=Work+Sans:wght@400;500&display=swap">
<style>
  :root {
    --backdrop: #141414;
    --card-top: #232323;
    --card-bottom: #1a1a1a;
    --mark-front: #7d7d7d;
    --mark-back: #0e0e0e;
    --foil: #e2e2e2;
    --foil-soft: #bdbdbd;
    --rule: #8a8a8a;
  }
  * { box-sizing: border-box; margin: 0; padding: 0; }
  html, body { width: 1200px; height: 900px; overflow: hidden; background: var(--backdrop); }
  .canvas {
    position: relative; width: 1200px; height: 900px;
    font-family: "Work Sans", Arial, sans-serif;
  }
  .card {
    position: absolute; left: 280px; width: 640px; height: 366px;
    background: linear-gradient(160deg, var(--card-top), var(--card-bottom));
    overflow: hidden;
  }
  .card--front { top: 70px; }
  .card--back { top: 470px; }

  .brand {
    display: flex; align-items: center; gap: 12px;
    font-weight: 500; line-height: 1.15; letter-spacing: 0.01em;
    white-space: nowrap;
  }
  .brand__square { width: 20px; height: 20px; flex: none; }
  .card--front .brand {
    position: absolute; left: 150px; top: 140px;
    font-size: 30px; color: var(--mark-front);
  }
  .card--front .brand__square { width: 22px; height: 22px; background: var(--mark-front); }
  .card--back .brand {
    position: absolute; left: 38px; top: 146px;
    font-size: 21px; color: var(--mark-back);
  }
  .card--back .brand__square { background: var(--mark-back); }

  .divider {
    position: absolute; left: 318px; top: 70px; width: 1px; height: 230px;
    background: var(--rule);
  }
  .holder { position: absolute; left: 348px; top: 74px; right: 16px; color: var(--foil); }
  .holder__name { font-size: 25px; font-weight: 500; letter-spacing: 0.09em; text-transform: uppercase; }
  .holder__role { font-size: 14px; color: var(--foil-soft); margin-top: 2px; letter-spacing: 0.04em; }
  .holder__address { font-size: 15px; line-height: 1.55; margin-top: 20px; color: var(--foil-soft); letter-spacing: 0.03em; }
  .contact-list { list-style: none; margin-top: 14px; font-size: 15px; letter-spacing: 0.03em; }
  .contact-list li { display: flex; align-items: center; gap: 10px; line-height: 1.7; color: var(--foil); white-space: nowrap; }
  .contact-list svg { width: 12px; height: 12px; flex: none; }
</style>
</head>
<body>
<main class="canvas">
  <section class="card card--front" aria-label="Card front">
    <div class="brand">
      <span class="brand__square"></span>
      <span class="brand__name">Real Estate<br>Summitline Partners</span>
    </div>
  </section>

  <section class="card card--back" aria-label="Card back">
    <div class="brand">
      <span class="brand__square"></span>
      <span class="brand__name">Real Estate<br>Summitline Partners</span>
    </div>
    <div class="divider"></div>
    <div class="holder">
      <h1 class="holder__name">Dorian Vale</h1>
      <p class="holder__role">Director</p>
      <p class="holder__address">4120 NE Larkspur Ave.<br>Suite 305-B,<br>Halvern, OR 97208</p>
      <ul class="contact-list">
        <li>
          <svg viewBox="0 0 12 12" aria-hidden="true"><path d="M2.5 1h2l1 2.5-1.3 1a6 6 0 0 0 3.3 3.3l1-1.3L11 7.5v2a1.5 1.5 0 0 1-1.5 1.5A8.5 8.5 0 0 1 1 2.5 1.5 1.5 0 0 1 2.5 1z" fill="#bdbdbd"/></svg>
          (555) 214-7730
        </li>
        <li>
          <svg viewBox="0 0 12 12" aria-hidden="true"><rect x="1" y="2.5" width="10" height="7" fill="none" stroke="#bdbdbd" stroke-width="1.1"/><path d="M1 2.5l5 4 5-4" fill="none" stroke="#bdbdbd" stroke-width="1.1"/></svg>
          dorianvale@summitline.example
        </li>
        <li>
          <svg viewBox="0 0 12 12" aria-hidden="true"><circle cx="6" cy="6" r="5" fill="none" stroke="#bdbdbd" stroke-width="1.1"/><ellipse cx="6" cy="6" rx="2.2" ry="5" fill="none" stroke="#bdbdbd" stroke-width="1"/><path d="M1 6h10" stroke="#bdbdbd" stroke-width="1"/></svg>
          www.summitlinehomes.example
        </li>
      </ul>
    </div>
  </section>
</main>
</body>
</html>
```